依頼詳細
オープン前のプレオープンで使用するチラシ依頼です。
キャンペーン価格で5日間限定で初回は初見料と施術代で9000円が500円1日限定で10名

こんなお困りの症状はありませんか?

・整体やマッサージに通っているが、肩がこって仕事や日常生活がつらい
・腰痛で電気をあてたり、整骨院に行っても変化がなく諦めている
・頻繁に頭痛に襲われて辛いので、その度に頭痛薬を飲む
・生理前後に痛みが強く、鎮痛薬を飲んでしまう
・精神薬を処方されたが、いつまで飲み続けるのか不安だけどやめられない
・病院で薬をもらったが一向にめまいが改善しない
の項目はなるべく全部入れたいです。

女性に特化した整体院なのでそこがイメージしやすいデザインがありがたいです。
記載項目
店名:自律神経専門 整体院 ゆらぎ→自律神経専門を目立たせて欲しいです。

URL:https://yuragi-karada.example/

地図→詳細を送りますので作成して頂きたいです。

スタッフ写真もしくは女性が施術している写真を入れて欲しいです。

マンションの外装写真を入れるか目印のマルカワ堂がすぐ近く(ビル1つとなり)なので場所イメージがついたほうがいい気がするのでそこの情報はどちらか入れたいです。
電話番号とラインに関しては7月中に取得します。

院内
・予約優先制
・女性セラピスト指名OK
・施術ルーム完全個室
・キッズスペースあり
・ロゴ
を入れたいです。

サイズ
A4
ページ数
両面
希望イメージ
シンプル 複雑
単色 カラフル
暗い 明るい
日常 高級
遊び心 厳粛
未来的 伝統的
女性的 男性的
希望する色
赤系、緑系、茶系
納品ファイル
• 高解像度JPG (.jpg)
• PNG形式 (.png)
補足説明
可能であれば当社でも内容を修正することができれば助かります。
出来る限りインパクトの強いチラシが希望です。

「自律神経専門」整体院の自律神経専門が目立ちたいです。
宜しくお願い致します。

```html
<!DOCTYPE html>
<html lang="ja">
<head>
<meta charset="utf-8">
<title>自律神経専門 整体院 ゆらぎ OPEN</title>
<link href="https://fonts.googleapis.com/css2?family=Shippori+Mincho+B1:wght@600;800&family=Zen+Maru+Gothic:wght@500;700;900&display=swap" rel="stylesheet">
<style>
  :root{
    --green:#8cbf45;
    --green-deep:#6fa52f;
    --green-pale:#c9e2a0;
    --green-mist:#eef6e2;
    --orange:#f0892a;
    --ink:#5b4a3b;
    --paper:#ffffff;
  }
  *{margin:0;padding:0;box-sizing:border-box}
  html,body{width:851px;height:1200px;overflow:hidden;background:var(--paper)}
  body{font-family:"Zen Maru Gothic",sans-serif;color:var(--ink)}
  .flyer{position:relative;width:851px;height:1200px;overflow:hidden;background:var(--paper)}

  .leaves{position:absolute;border-radius:50%;filter:blur(2px)}
  .leaves--top-left{left:-60px;top:-50px;width:240px;height:180px;background:radial-gradient(circle,var(--green-pale),rgba(201,226,160,0) 70%)}
  .leaves--top-right{right:-40px;top:-40px;width:220px;height:200px;background:radial-gradient(circle,var(--green-pale),rgba(201,226,160,0) 70%)}
  .leaves--bottom-left{left:-70px;bottom:-60px;width:260px;height:240px;background:radial-gradient(circle,var(--green-pale),rgba(201,226,160,0) 70%)}

  .portrait{position:absolute;left:340px;top:0;width:511px;height:570px;
    background:linear-gradient(160deg,#f4f1ec 0%,#e9dfd4 45%,#d8c7b6 100%)}

  .hero-circle{position:absolute;left:30px;top:30px;width:400px;height:400px;border-radius:50%;
    background:var(--green-pale);opacity:.95}
  .catch{position:absolute;left:30px;top:70px;width:400px;text-align:center;
    font-family:"Shippori Mincho B1",serif;font-weight:800;color:var(--ink)}
  .catch__line{display:block;font-size:34px;line-height:1.45;letter-spacing:.04em}
  .catch__line--white{color:#fff;text-shadow:0 0 2px rgba(111,165,47,.4)}
  .specialty{position:absolute;left:50px;top:200px;width:360px;height:200px;
    background:var(--green);color:#fff;text-align:center;
    font-family:"Shippori Mincho B1",serif;font-weight:800;font-size:72px;line-height:92px;padding-top:8px;letter-spacing:.06em}

  .clinic-name{position:absolute;left:60px;top:480px;width:340px;text-align:center}
  .clinic-name__mark{display:block;margin:0 auto 10px;width:44px;height:44px;border-radius:50%;background:var(--green)}
  .clinic-name__text{font-family:"Shippori Mincho B1",serif;font-weight:800;font-size:40px;color:var(--ink);letter-spacing:.08em}

  .open-date{position:absolute;left:60px;top:650px;color:var(--green-deep);font-family:"Zen Maru Gothic",sans-serif;font-weight:900}
  .open-date__year{display:block;font-size:26px;letter-spacing:.05em}
  .open-date__note{position:absolute;left:220px;top:-6px;font-size:22px;font-weight:700;transform:rotate(-6deg);white-space:nowrap}
  .open-date__main{display:flex;align-items:flex-end;gap:6px;margin-top:-4px}
  .open-date__day{font-size:96px;line-height:1;letter-spacing:-.02em}
  .open-date__dow{font-size:20px;margin-bottom:14px;writing-mode:horizontal-tb}
  .open-date__word{font-size:82px;line-height:1;letter-spacing:.02em}

  .treatment-scene{position:absolute;left:585px;top:575px;width:230px;height:130px;border-radius:12px;
    background:linear-gradient(135deg,#fbeee4,#f3dccb)}

  .campaign{position:absolute;left:560px;top:710px;width:250px;height:112px;border:3px solid var(--orange);border-radius:6px;background:#fff}
  .campaign__label{position:absolute;left:60px;top:-18px;background:var(--orange);color:#fff;font-size:16px;font-weight:900;padding:4px 12px;border-radius:4px;white-space:nowrap}
  .campaign__badge{position:absolute;left:-40px;top:-10px;width:64px;height:64px;border-radius:50%;background:var(--orange);color:#fff;
    font-size:13px;font-weight:900;text-align:center;line-height:1.2;padding-top:14px}
  .campaign__badge b{font-size:22px}
  .campaign__regular{position:absolute;left:28px;top:30px;font-size:12px;font-weight:700;line-height:1.3}
  .campaign__regular b{font-size:20px;color:var(--ink)}
  .campaign__limit{position:absolute;right:12px;top:26px;font-size:11px;font-weight:700}
  .campaign__price{position:absolute;right:12px;top:42px;color:var(--orange);font-size:52px;font-weight:900;line-height:1}
  .campaign__price small{font-size:22px}
  .campaign__arrow{position:absolute;left:118px;top:64px}

  .symptoms{position:absolute;left:40px;top:818px;width:500px}
  .symptoms__title{font-family:"Shippori Mincho B1",serif;font-weight:800;font-size:23px;color:var(--ink);margin-bottom:12px}
  .symptoms__list{list-style:none}
  .symptoms__item{display:flex;align-items:flex-start;gap:8px;font-size:13.5px;font-weight:500;line-height:1.5;margin-bottom:8px;border-bottom:1px dotted var(--green-pale);padding-bottom:4px}
  .symptoms__check{flex:none;margin-top:3px}

  .consult{position:absolute;left:562px;top:858px;width:260px;font-family:"Shippori Mincho B1",serif;font-weight:800}
  .consult__line{display:block;font-size:22px;line-height:1.5;color:var(--ink)}
  .consult__line--small{font-size:17px}
  .consult__band{display:inline-block;margin:6px 0;background:var(--green);color:#fff;font-size:25px;padding:2px 10px;letter-spacing:.04em}
  .consult__rule{display:block;width:250px;height:2px;background:var(--green);margin-top:10px}

  .next-page{position:absolute;right:40px;top:1110px;font-size:13px;font-weight:700;color:var(--ink)}
  .next-page::after{content:" →"}
</style>
</head>
<body>
<main class="flyer">
  <div class="leaves leaves--top-left" role="img" aria-label="淡い緑の葉のあしらい"></div>
  <div class="leaves leaves--top-right" role="img" aria-label="淡い緑の葉のあしらい"></div>
  <div class="leaves leaves--bottom-left" role="img" aria-label="淡い緑の葉のあしらい"></div>

  <div class="portrait" role="img" aria-label="笑顔の女性スタッフの写真"></div>

  <div class="hero-circle"></div>
  <h2 class="catch">
    <span class="catch__line catch__line--white">あきらめていた</span>
    <span class="catch__line catch__line--white">女性の悩みを改善!</span>
  </h2>
  <h1 class="specialty">自律神経<br>専門</h1>

  <div class="clinic-name">
    <span class="clinic-name__mark"></span>
    <span class="clinic-name__text">整体院 ゆらぎ</span>
  </div>

  <div class="open-date">
    <span class="open-date__year">2020</span>
    <span class="open-date__note">〇〇駅前に</span>
    <div class="open-date__main">
      <span class="open-date__day">9/00</span>
      <span class="open-date__dow">SUN</span>
      <span class="open-date__word">OPEN</span>
    </div>
  </div>

  <div class="treatment-scene" role="img" aria-label="女性セラピストが施術しているイラスト"></div>

  <div class="campaign">
    <span class="campaign__badge"><b>5</b>日間<br>限定</span>
    <span class="campaign__label">OPEN キャンペーン</span>
    <p class="campaign__regular">初見料+施術代<br><b>9,000</b>円が</p>
    <svg class="campaign__arrow" width="16" height="20" viewBox="0 0 16 20"><path d="M2 2 L12 10 L2 18" fill="none" stroke="#f0892a" stroke-width="3"/></svg>
    <p class="campaign__limit">1日10名まで</p>
    <p class="campaign__price">500<small>円</small></p>
  </div>

  <section class="symptoms">
    <h3 class="symptoms__title">こんなお困りの症状はありませんか?</h3>
    <ul class="symptoms__list">
      <li class="symptoms__item"><svg class="symptoms__check" width="14" height="14" viewBox="0 0 14 14"><rect x="1" y="1" width="12" height="12" fill="none" stroke="#6fa52f" stroke-width="1.5"/><path d="M3 7 L6 10 L12 2" fill="none" stroke="#6fa52f" stroke-width="2"/></svg>整体やマッサージに通っているが、肩がこって仕事や日常生活がつらい</li>
      <li class="symptoms__item"><svg class="symptoms__check" width="14" height="14" viewBox="0 0 14 14"><rect x="1" y="1" width="12" height="12" fill="none" stroke="#6fa52f" stroke-width="1.5"/><path d="M3 7 L6 10 L12 2" fill="none" stroke="#6fa52f" stroke-width="2"/></svg>腰痛で電気をあてたり、整骨院に行っても変化がなく諦めている</li>
      <li class="symptoms__item"><svg class="symptoms__check" width="14" height="14" viewBox="0 0 14 14"><rect x="1" y="1" width="12" height="12" fill="none" stroke="#6fa52f" stroke-width="1.5"/><path d="M3 7 L6 10 L12 2" fill="none" stroke="#6fa52f" stroke-width="2"/></svg>頻繁に頭痛に襲われて辛いので、その度に頭痛薬を飲む</li>
      <li class="symptoms__item"><svg class="symptoms__check" width="14" height="14" viewBox="0 0 14 14"><rect x="1" y="1" width="12" height="12" fill="none" stroke="#6fa52f" stroke-width="1.5"/><path d="M3 7 L6 10 L12 2" fill="none" stroke="#6fa52f" stroke-width="2"/></svg>生理前後に痛みが強く、鎮痛薬を飲んでしまう</li>
      <li class="symptoms__item"><svg class="symptoms__check" width="14" height="14" viewBox="0 0 14 14"><rect x="1" y="1" width="12" height="12" fill="none" stroke="#6fa52f" stroke-width="1.5"/><path d="M3 7 L6 10 L12 2" fill="none" stroke="#6fa52f" stroke-width="2"/></svg>精神薬を処方されたが、いつまで飲み続けるのか不安だけどやめられない</li>
      <li class="symptoms__item"><svg class="symptoms__check" width="14" height="14" viewBox="0 0 14 14"><rect x="1" y="1" width="12" height="12" fill="none" stroke="#6fa52f" stroke-width="1.5"/><path d="M3 7 L6 10 L12 2" fill="none" stroke="#6fa52f" stroke-width="2"/></svg>病院で薬をもらったが一向にめまいが改善しない</li>
    </ul>
  </section>

  <section class="consult">
    <span class="consult__line">今までにない</span>
    <span class="consult__line consult__line--small">女性特有の悩みに特化した</span>
    <span class="consult__band">自律神経専門の</span>
    <span class="consult__line">当院にご相談ください!</span>
    <span class="consult__rule"></span>
  </section>

  <p class="next-page">詳しくは裏面へ</p>
</main>
</body>
</html>
```